Web Site Design for KORA@DBC, an innovative energy research group

The Kinetic Ohm Research Annex at the Dalbrook College (KORA@DBC) is a research group in Vermont that is working to make electricity cleaner, more reliable and more affordable. We are looking for a web site design (preferably based on Wordpress or a similar content management system) that highlights the following themes:
* Renewable energy: particularly wind and solar
* Electric energy (images of cities at night, for example)
* Distributed energy (e.g., rooftop solar systems on houses)
* Bertil Hallgren. We have previously used a version of this image
https://archive.pictorvault.example/item/File:Bertil_Hallgren,_with_his_apparatus_Marrow_Q0027391.jpg
which is in the public domain, in an early draft of our site. This early version of the site is located here:
http://blog.dalbrookcoll.example/hallgren/
* The Dalbrook College. Images that we can use for this site are located here:
http://dbcpics.snapmerit.example/gallery-collection/DBC-Campus-Scenic-Images/X0000Q_7k2pR5zLm

We would like the site map to roughly follow the following:
* Home (link should be labeled: KORA@DBC)
The home page should include
some relevant imagery at the top,
a section for blog posts on the left side
a sidebar on the right that includes twitter feeds for @quentinrowedbc and @thevoltfinches
A placeholder section at the bottom labeled “acknowledgements”
* About. Include only placeholder text here. We can compose the text content
* People. This page should have placeholder boxes for three sets of people
Faculty
Students
Alumni
* Projects. The projects link should go to a dropdown menu list of different projects. These can be labeled Project 1, Project 2, Project 3 for now, and then we can edit the content later.
* Publications. This page should be a list of publications organized in a table with one image to the left of each paper. We can provide the content.

Some research group sites that we like include:
http://www.gilesmorrow.example/
https://pwrx.haldane.example/
http://kvt.marsby.example/

We would also be interested to include a relatively simple team logo that features our abbreviated name (KORA@DBC) and potentially some symbol of energy innovation. E.g., light bulbs, tesla coils, etc.

Target Market(s)

University researchers, graduate students, electric energy professionals

Industry/Entity Type

Laboratory

Logo Text

KORA@DBC

Coding

Coded - Design and coding required

Number of Pages Required

5+ page

Font styles to use
Sans Serif

Requirements
Must have
• Creative imagery that symbolize what we are doing.
Nice to have
• Some sort of content management system (though we can work with raw html/css if needed).

```html
<!DOCTYPE html>
<html lang="en">
<head>
<meta charset="utf-8">
<title>KORA@DBC — The Kinetic Ohm Research Annex</title>
<link href="https://fonts.googleapis.com/css2?family=Lato:wght@300;400;700&display=swap" rel="stylesheet">
<style>
:root{
  --ink:#333;
  --muted:#8a8a8a;
  --body:#777;
  --accent:#2f8fd8;
  --line:#e4e4e4;
  --footer:#f3f3f3;
  --share:#4a70b8;
  --hero-top:#1e6fc9;
  --hero-bottom:#7fc0ee;
  --white:#fff;
}
*{box-sizing:border-box;margin:0;padding:0}
html,body{width:1200px;height:2488px;overflow:hidden;background:var(--white)}
body{position:relative;font-family:'Lato',sans-serif;color:var(--ink)}
.abs{position:absolute}

/* header */
.site-header{left:0;top:0;width:1200px;height:100px;border-bottom:1px solid var(--line)}
.brand{left:130px;top:22px}
.brand-name{font-size:34px;font-weight:400;letter-spacing:1px;color:var(--ink);line-height:1}
.brand-tag{font-size:11px;color:var(--ink);margin-top:8px}
.main-nav{right:180px;top:60px;display:flex;gap:34px;font-size:11px;letter-spacing:1px;text-transform:uppercase;color:var(--muted)}
.main-nav .current{color:var(--accent);border-bottom:2px solid var(--accent);padding-bottom:8px}
.search-icon{right:130px;top:22px}

/* hero */
.hero{left:0;top:100px;width:1200px;height:470px;background:linear-gradient(160deg,var(--hero-top) 0%,#3c8fdc 45%,var(--hero-bottom) 100%)}
.hero-title{left:130px;top:282px;font-size:38px;font-weight:300;letter-spacing:3px;color:var(--white)}
.hero-text{left:130px;top:338px;width:420px;font-size:12px;line-height:18px;color:#e6f1fb}
.hero-arrow{top:318px;width:34px;height:48px;background:rgba(80,80,80,.45)}
.hero-arrow.prev{left:0}
.hero-arrow.next{right:0}

/* posts */
.post-title{left:130px;font-size:30px;font-weight:400;letter-spacing:2px;color:var(--ink)}
.post-date{left:130px;font-size:11px;color:var(--muted)}
.post-excerpt{left:130px;width:600px;font-size:12px;line-height:18px;color:var(--body)}
.post-photo{left:130px;width:600px;height:260px}
.share{left:130px;display:flex;gap:6px}
.share span{display:block;width:44px;height:16px;background:var(--share);color:var(--white);font-size:9px;line-height:16px;text-align:center;border-radius:2px}
.next-link{left:130px;top:2166px;font-size:11px;letter-spacing:1px;color:var(--ink)}

/* sidebar */
.side-title{left:790px;width:280px;font-size:20px;letter-spacing:2px;font-weight:400;padding-bottom:14px;border-bottom:1px solid var(--line)}
.tweet{left:790px;width:280px;display:flex;gap:18px}
.avatar{width:64px;height:64px;background:#9a8a7c;flex:none}
.tweet-body{font-size:11px;line-height:16px;color:var(--body)}
.tweet-name{color:var(--accent)}
.tweet-handle{color:var(--ink)}
.badges{left:800px;top:1068px;width:260px}

/* footer */
.site-footer{left:0;top:2200px;width:1200px;height:288px;background:var(--footer)}
.foot-brand{left:130px;top:2248px;font-size:34px;letter-spacing:1px;color:var(--ink)}
.social{left:130px;top:2296px;display:flex;gap:8px}
.social span{display:block;width:24px;height:24px;border:2px solid var(--ink);border-radius:50%}
.foot-col{top:2222px;font-size:11px;color:var(--body);line-height:20px}
.foot-col h4{font-size:11px;letter-spacing:1px;color:var(--ink);font-weight:700;margin-bottom:6px;text-transform:uppercase}
.foot-input{width:200px;height:28px;background:var(--white);border:1px solid var(--line);font-size:10px;color:var(--muted);padding:6px 10px;margin-top:10px}
.foot-button{width:80px;height:24px;background:var(--accent);color:var(--white);font-size:10px;line-height:24px;text-align:center;margin-top:12px}
.contact-row{display:flex;gap:8px;align-items:center}
.contact-row i{display:block;width:10px;height:10px;background:var(--accent);border-radius:2px}
.foot-rule{left:130px;top:2428px;width:940px;border-top:1px solid #dcdcdc}
.copyright{left:0;top:2450px;width:1200px;text-align:center;font-size:10px;color:var(--muted)}
</style>
</head>
<body>

<header class="site-header abs">
  <div class="brand abs">
    <div class="brand-name">KORA@DBC</div>
    <div class="brand-tag">The Kinetic Ohm Research Annex in Vermont</div>
  </div>
  <nav class="main-nav abs">
    <span class="current">Home</span><span>People</span><span>Projects</span><span>Photos</span><span>Our Environmental</span><span>Programs</span>
  </nav>
  <svg class="search-icon abs" width="16" height="16" viewBox="0 0 16 16" aria-label="Search"><circle cx="6.5" cy="6.5" r="5" fill="none" stroke="#888" stroke-width="1.6"/><line x1="10.2" y1="10.2" x2="15" y2="15" stroke="#888" stroke-width="1.8"/></svg>
</header>

<section class="hero abs" role="img" aria-label="Wind turbine against a bright blue sky"></section>
<h1 class="hero-title abs">RENEWABLE ENERGY</h1>
<p class="hero-text abs">We are a research group in Vermont that is working to make electricity cleaner, more reliable and more affordable.</p>
<div class="hero-arrow prev abs"><svg width="34" height="48" viewBox="0 0 34 48"><polyline points="20,18 14,24 20,30" fill="none" stroke="#fff" stroke-width="2"/></svg></div>
<div class="hero-arrow next abs"><svg width="34" height="48" viewBox="0 0 34 48"><polyline points="14,18 20,24 14,30" fill="none" stroke="#fff" stroke-width="2"/></svg></div>

<!-- posts -->
<h2 class="post-title abs" style="top:612px">WIND AND SOLAR</h2>
<div class="post-date abs" style="top:662px">15 Mar, 2017</div>
<p class="post-excerpt abs" style="top:696px">Neque porro quisquam est, qui dolorem ipsum quia dolor sit amet, consectetur, adipisci velit, sed quia non numquam eius modi tempora incidunt ut labore et dolore magnam aliquam quaerat voluptatem. Ut enim ad minima veniam.</p>
<div class="post-photo abs" style="top:792px;background:linear-gradient(150deg,#1d6ccf,#8cc6f2 60%,#d9ecfa)" role="img" aria-label="Solar panels and a wind turbine under a blue sky"></div>
<div class="share abs" style="top:1076px"><span>Like</span><span>Share</span></div>

<h2 class="post-title abs" style="top:1160px">ELECTRIC ENERGY</h2>
<div class="post-date abs" style="top:1210px">15 Mar, 2017</div>
<p class="post-excerpt abs" style="top:1244px">Neque porro quisquam est, qui dolorem ipsum quia dolor sit amet, consectetur, adipisci velit, sed quia non numquam eius modi tempora incidunt ut labore et dolore magnam aliquam quaerat voluptatem. Ut enim ad minima veniam.</p>
<div class="post-photo abs" style="top:1320px;height:272px;background:linear-gradient(180deg,#b9d3d6,#5f8d93 55%,#2f5a62)" role="img" aria-label="Row of offshore wind turbines over the sea"></div>
<div class="share abs" style="top:1608px"><span>Like</span><span>Share</span></div>

<h2 class="post-title abs" style="top:1680px">THE KINETIC OHM RESEARCH ANNEX</h2>
<div class="post-date abs" style="top:1730px">15 Mar, 2017</div>
<p class="post-excerpt abs" style="top:1764px">Neque porro quisquam est, qui dolorem ipsum quia dolor sit amet, consectetur, adipisci velit, sed quia non numquam eius modi tempora incidunt ut labore et dolore magnam aliquam quaerat voluptatem.</p>
<div class="post-photo abs" style="top:1848px;background:linear-gradient(180deg,#3d8fe0,#a9d2f3 40%,#4a6a8c 62%,#5f9a3a 85%,#4c8a2c)" role="img" aria-label="Solar panel array on a green field under cloudy sky"></div>
<div class="next-link abs">NEXT »</div>

<!-- sidebar -->
<h3 class="side-title abs" style="top:620px">TWEETS</h3>
<div class="tweet abs" style="top:690px">
  <div class="avatar" role="img" aria-label="Profile photo"></div>
  <div class="tweet-body"><div class="tweet-name">Lorem ipsum dolor</div><div class="tweet-handle">@quentinrowedbc</div>Neque porro quisquam est qui dolorem ipsum quia dolor sit amet, consectetur, adipisci velit voluptatem.</div>
</div>
<div class="tweet abs" style="top:846px">
  <div class="avatar" role="img" aria-label="Profile photo" style="background:#8d8478"></div>
  <div class="tweet-body"><div class="tweet-name">Lorem ipsum dolor</div><div class="tweet-handle">@thevoltfinches</div>Neque porro quisquam est qui dolorem ipsum quia dolor sit amet, consectetur, adipisci velit voluptatem.</div>
</div>

<h3 class="side-title abs" style="top:1000px">ACKNOWLEDGEMENT</h3>
<svg class="badges abs" width="260" height="150" viewBox="0 0 260 150" aria-label="Partner badges">
  <circle cx="38" cy="36" r="28" fill="#2b4a8a"/>
  <circle cx="130" cy="36" r="28" fill="#1f6f9e"/>
  <circle cx="222" cy="36" r="28" fill="#223a5e"/>
  <circle cx="84" cy="116" r="28" fill="#2a3f7a"/>
  <circle cx="176" cy="116" r="28" fill="#3a3a3a"/>
</svg>

<!-- footer -->
<footer class="site-footer abs"></footer>
<div class="foot-brand abs">KORA@DBC</div>
<div class="social abs"><span></span><span></span><span></span><span></span><span></span></div>
<div class="foot-col abs" style="left:432px">
  <h4>Quick Links</h4>
  Home<br>People<br>Publications<br>Projects<br>Photos<br>Our Environmental<br>Programs
</div>
<div class="foot-col abs" style="left:580px;width:240px">
  <h4>Newsletter</h4>
  Enter your email address to receive the latest news and notes from our blog.
  <div class="foot-input">Enter Your Email</div>
  <div class="foot-button">Subscribe</div>
</div>
<div class="foot-col abs" style="left:904px">
  <h4>Contact Us</h4>
  <div class="contact-row"><i></i>(802) 555-0147</div>
  <div class="contact-row"><i></i>(802) 555-0182</div>
  <div class="contact-row"><i></i>info@kora-dbc.example</div>
  <div class="contact-row"><i></i>12 Orchard Row, Dalbrook</div>
</div>
<div class="foot-rule abs"></div>
<div class="copyright abs">© 2017 KORA@DBC. All Rights Reserved.</div>

</body>
</html>
```